Business cards for Wendcycle

We need a business card layout for our new bike and e-bike rental (we also sell used e-bikes and bike accessories). The logo already exists.

```html
<!DOCTYPE html>
<html lang="de">
<head>
<meta charset="utf-8">
<title>Wendcycle – Visitenkarte</title>
<link href="https://fonts.googleapis.com/css2?family=Open+Sans:wght@300;400;600&display=swap" rel="stylesheet">
<style>
  :root {
    --page-bg: #e6e7e8;
    --card-dark: #1b3039;
    --card-light: #f2f1f1;
    --accent: #5cc4a0;
    --text-light: #f2f4f4;
    --text-dark: #1f3139;
  }
  * { margin: 0; padding: 0; box-sizing: border-box; }
  html, body {
    width: 1200px; height: 900px; overflow: hidden;
    background: var(--page-bg);
    font-family: "Open Sans", Arial, sans-serif;
  }
  .stage {
    width: 1200px; height: 900px;
    display: flex; align-items: center; justify-content: center;
  }
  .card {
    width: 960px; height: 590px;
    display: flex;
    box-shadow: 0 10px 30px rgba(0,0,0,0.18);
  }
  .card-contact {
    width: 472px; height: 100%;
    background: var(--card-dark);
    color: var(--text-light);
    padding: 88px 0 0 58px;
  }
  .person-name {
    color: var(--accent);
    font-size: 33px; font-weight: 600;
    letter-spacing: 0.5px; line-height: 1.1;
  }
  .person-role {
    font-size: 27px; font-weight: 400; line-height: 1.3;
  }
  .contact-list {
    list-style: none;
    margin-top: 132px;
  }
  .contact-list li {
    display: flex; align-items: center;
    font-size: 27px; line-height: 35px;
  }
  .contact-icon {
    width: 22px; height: 22px; margin-right: 12px;
    fill: var(--accent); flex: none;
  }
  .address {
    font-style: normal;
    font-size: 27px; line-height: 35px;
    margin-top: 14px;
  }
  .accent-stripe {
    width: 12px; height: 100%;
    background: var(--accent);
  }
  .card-brand {
    flex: 1; height: 100%;
    background: var(--card-light);
    display: flex; flex-direction: column;
    align-items: center; justify-content: center;
    padding-top: 60px;
  }
  .brand-name {
    color: var(--accent);
    font-size: 74px; font-weight: 300;
    letter-spacing: 1px; line-height: 1;
  }
  .brand-tagline {
    color: var(--text-dark);
    font-size: 25px; font-weight: 600;
    margin-top: 48px;
  }
</style>
</head>
<body>
<main class="stage">
  <article class="card">
    <section class="card-contact">
      <h1 class="person-name">JONAS WEBER</h1>
      <p class="person-role">Managing Director</p>
      <ul class="contact-list">
        <li>
          <svg class="contact-icon" viewBox="0 0 24 24" aria-hidden="true"><path d="M3 9c0-3 4-5 9-5s9 2 9 5v2h-5V9c-1-1-7-1-8 0v2H3z"/><rect x="5" y="12" width="14" height="8" rx="2"/></svg>
          031-555 208 417
        </li>
        <li>
          <svg class="contact-icon" viewBox="0 0 24 24" aria-hidden="true"><path d="M8 2h8a2 2 0 0 1 2 2v16a2 2 0 0 1-2 2H8a2 2 0 0 1-2-2V4a2 2 0 0 1 2-2zm0 3v13h8V5zm4 14.2a1 1 0 1 0 0 1.6 1 1 0 0 0 0-1.6z"/></svg>
          079-555 318 642
        </li>
        <li>
          <svg class="contact-icon" viewBox="0 0 24 24" aria-hidden="true"><path d="M2 6h20v1l-10 6L2 7zm0 3 10 6 10-6v10H2z"/></svg>
          info@wendcycle.com
        </li>
        <li>
          <svg class="contact-icon" viewBox="0 0 24 24" aria-hidden="true"><circle cx="12" cy="12" r="10"/><path d="M7 8c2 0 3 1 3 3s2 2 2 4-1 3-2 4M15 5c0 2 1 3 3 3" stroke="#1b3039" stroke-width="2" fill="none"/></svg>
          www.wendcycle.com
        </li>
      </ul>
      <address class="address">
        48 Veloweg, Hafenviertel<br>
        Nordland, 482019.
      </address>
    </section>
    <div class="accent-stripe"></div>
    <section class="card-brand">
      <p class="brand-name">WENDCYCLE</p>
      <p class="brand-tagline">e-leicht unterwegs</p>
    </section>
  </article>
</main>
</body>
</html>
```